Business Card Design

Electronic Security
Alarm Systems
CCTV
Electronic Access Control
Security System Integration

Industry/Entity Type

Business

Contact Information for Business Card

Declan Whitfield
PO Box 862
Carrowbrook Qld 4179
Phone 07 38265014
Mob 0428615937

```html
<!DOCTYPE html>
<html lang="en">
<head>
<meta charset="utf-8">
<title>Arvell Business Card</title>
<link href="https://fonts.googleapis.com/css2?family=Arimo:wght@400;700&display=swap" rel="stylesheet">
<style>
  :root {
    --bg-light: #e4e4e4;
    --bg-dark: #a9a9a9;
    --card: #ffffff;
    --ink: #1c1c1c;
    --brand: #1f9ad6;
    --orange-a: #ffc21a;
    --orange-b: #f06a24;
    --blue-a: #12a6e6;
    --blue-b: #3a3f47;
  }
  html, body {
    margin: 0;
    width: 1200px;
    height: 1170px;
    overflow: hidden;
  }
  body {
    background: radial-gradient(ellipse at 50% 20%, var(--bg-light) 0%, var(--bg-dark) 100%);
    font-family: "Arimo", Arial, sans-serif;
    color: var(--ink);
    position: relative;
  }
  .card {
    position: absolute;
    left: 130px;
    top: 295px;
    width: 940px;
    height: 580px;
    background: var(--card);
    box-shadow: 0 18px 40px rgba(0,0,0,0.28);
    overflow: hidden;
  }
  .card-facets {
    position: absolute;
    inset: 0;
  }
  .brand {
    position: absolute;
    left: 70px;
    top: 250px;
    display: flex;
    align-items: center;
    gap: 16px;
  }
  .brand-square {
    width: 34px;
    height: 34px;
    background: var(--brand);
  }
  .brand-name {
    font-size: 58px;
    font-weight: 400;
    color: var(--ink);
    letter-spacing: 2px;
    line-height: 1;
  }
  .services {
    position: absolute;
    right: 260px;
    top: 190px;
    margin: 0;
    padding: 0;
    list-style: none;
    text-align: right;
    font-size: 23px;
    line-height: 30px;
  }
  .contact {
    position: absolute;
    left: 70px;
    top: 395px;
    margin: 0;
    font-size: 20px;
    line-height: 29px;
    font-style: normal;
  }
  .contact-label {
    font-weight: 700;
  }
</style>
</head>
<body>
  <section class="card" aria-label="Business card">
    <svg class="card-facets" width="940" height="580" viewBox="0 0 940 580" aria-hidden="false">
      <defs>
        <linearGradient id="facet-orange" x1="0" y1="0" x2="1" y2="1">
          <stop offset="0" stop-color="var(--orange-a)"/>
          <stop offset="1" stop-color="var(--orange-b)"/>
        </linearGradient>
        <linearGradient id="facet-blue" x1="0" y1="1" x2="1" y2="0">
          <stop offset="0" stop-color="var(--blue-a)"/>
          <stop offset="0.5" stop-color="var(--blue-b)"/>
          <stop offset="1" stop-color="var(--blue-a)"/>
        </linearGradient>
      </defs>
      <polygon role="img" aria-label="Orange faceted corner decoration"
               points="650,0 940,0 940,185 905,160 890,95 815,50"
               fill="url(#facet-orange)"/>
      <polygon role="img" aria-label="Blue and charcoal faceted decoration"
               points="940,180 940,580 355,580 470,440 650,440 835,225 905,165"
               fill="url(#facet-blue)"/>
    </svg>

    <div class="brand">
      <span class="brand-square" aria-hidden="true"></span>
      <span class="brand-name">ARVELL</span>
    </div>

    <ul class="services">
      <li>Electronic Security</li>
      <li>Alarm Systems</li>
      <li>CCTV</li>
      <li>Electronic Access Control</li>
      <li>Security System Integration</li>
    </ul>

    <address class="contact">
      <div><span class="contact-label">Address:</span> Declan Whitfield</div>
      <div>PO Box 862</div>
      <div>Carrowbrook Qld 4179</div>
      <div><span class="contact-label">Phone:</span> 07 38265014</div>
      <div><span class="contact-label">Mob:</span> 0428615937</div>
    </address>
  </section>
</body>
</html>
```